Progressive/contemporary business card design for successful Startups as a Service Company

New logo launched in 2020. New website launched in 2021. Now that COVID is (mostly) behind us, I'm networking with more people and need a business card that matches the company/logo design aesthetic.

```html
<!DOCTYPE html>
<html lang="en">
<head>
<meta charset="UTF-8">
<title>Brightlane Business Card</title>
<link href="https://fonts.googleapis.com/css2?family=Montserrat:wght@400;500;600;700&display=swap" rel="stylesheet">
<style>
  :root{
    --stage:#1e1e1e;
    --card-back:#2b2a28;
    --card-front:#ffffff;
    --ink:#1c1c1c;
    --ink-soft:#3a4456;
    --name-blue:#1a7bc4;
    --icon-red:#e0262b;
    --band:#1a7bc4;
  }
  *{margin:0;padding:0;box-sizing:border-box}
  html,body{width:1200px;height:1021px;overflow:hidden;background:var(--stage)}
  body{font-family:"Montserrat",sans-serif;position:relative}
  .card{
    position:absolute;left:290px;width:620px;height:354px;
    border-radius:2px;box-shadow:0 10px 30px rgba(0,0,0,.45);overflow:hidden;
  }
  .card--back{top:110px;background:var(--card-back);display:flex;align-items:center;justify-content:center;gap:14px}
  .card--front{top:524px;background:var(--card-front)}
  .brand-name{font-family:"Montserrat",sans-serif;font-weight:500;letter-spacing:.28em;text-transform:uppercase}
  .card--back .brand-name{color:#ffffff;font-size:34px}
  .brand-square{width:18px;height:18px;background:#ffffff}
  .card--front .brand{position:absolute;left:44px;top:44px;display:flex;align-items:center;gap:12px}
  .card--front .brand-name{color:var(--ink-soft);font-size:28px}
  .card--front .brand-square{background:var(--ink-soft);width:15px;height:15px}
  .person{position:absolute;left:44px;top:130px}
  .person-name{color:var(--name-blue);font-weight:700;font-size:22px;line-height:1.1}
  .person-title{color:var(--ink);font-weight:500;font-size:15px;margin-top:4px}
  .contact{position:absolute;left:330px;top:174px;color:var(--ink);font-size:16px;font-weight:500;line-height:1.3}
  .address{margin-bottom:10px}
  .contact-row{display:flex;align-items:center;gap:8px}
  .contact-row svg{width:15px;height:15px;flex:none}
  .base-band{position:absolute;left:0;bottom:0;width:100%;height:12px;background:var(--band)}
</style>
</head>
<body>
  <section class="card card--back" aria-label="Card back">
    <span class="brand-square"></span>
    <span class="brand-name">Brightlane</span>
  </section>

  <section class="card card--front" aria-label="Card front">
    <div class="brand">
      <span class="brand-name">Brightlane</span>
      <span class="brand-square"></span>
    </div>

    <div class="person">
      <div class="person-name">Daniel Reyes</div>
      <div class="person-title">Managing Director</div>
    </div>

    <div class="contact">
      <div class="address">418 Harbor Street<br>Tampa, Florida, 33602</div>
      <div class="contact-row">
        <svg viewBox="0 0 16 16" aria-hidden="true"><path d="M4 1.5l2.2 3-1.3 1.4c.8 1.8 2.3 3.3 4.1 4.1l1.4-1.3 3 2.2-1.2 2.5C7.6 13.2 2.8 8.4 1.6 2.7z" fill="none" stroke="var(--icon-red)" stroke-width="1.5" stroke-linejoin="round"/></svg>
        <span>(555) 214-0386</span>
      </div>
      <div class="contact-row">
        <svg viewBox="0 0 16 16" aria-hidden="true"><rect x="1" y="3" width="14" height="10" fill="none" stroke="var(--icon-red)" stroke-width="1.5"/><path d="M1 3l7 6 7-6M1 13l5-5M15 13l-5-5" fill="none" stroke="var(--icon-red)" stroke-width="1.3"/></svg>
        <span>daniel@brightlane.co</span>
      </div>
      <div class="contact-row">
        <svg viewBox="0 0 16 16" aria-hidden="true"><g fill="none" stroke="var(--icon-red)" stroke-width="1.3"><circle cx="8" cy="8" r="6.5"/><ellipse cx="8" cy="8" rx="3" ry="6.5"/><path d="M1.5 8h13M2.5 4.5h11M2.5 11.5h11"/></g></svg>
        <span>www.brightlane.co</span>
      </div>
    </div>

    <div class="base-band" aria-hidden="true"></div>
  </section>
</body>
</html>
```